New custom software business needs a Wordpress site

We need a Wordpress site for a new company based out of Chicago called 'Vellora Consulting'. Using a mix of on and off-shore resources we build custom software solutions, mainly focusing on small to medium sized companies. We help our customers "aspire" to do great things.
We have a basic site up here: https://brindlewave.example/. We worked on the content for it but not the branding. For now, this houses all the pages (except for a Contact Us page we'll be adding soon) for the foreseeable future.
We also have a new logo (attached) that we'd like to base the styling/colors on.
Target Market(s)
Small to medium sized companies that require tech resources
Industry/Entity Type
Software
Nice to have
- Teamwork, tech, professional but not elitist

```html
<!DOCTYPE html>
<html lang="en">
<head>
<meta charset="utf-8">
<title>Vellora Consulting</title>
<link href="https://fonts.googleapis.com/css2?family=Jost:wght@400;500;600&family=Poppins:wght@400;500&display=swap" rel="stylesheet">
<style>
:root{
  --blue:#0a50ad;
  --blue-dark:#083f88;
  --blue-soft:#2f6cc0;
  --ink:#2e2e2e;
  --muted:#555a60;
  --footer-bg:#eef1f5;
  --white:#ffffff;
}
*{box-sizing:border-box;margin:0;padding:0}
html,body{width:1200px;height:3778px;overflow:hidden;background:var(--white)}
body{position:relative;font-family:"Poppins",sans-serif;color:var(--muted)}
.abs{position:absolute}
a{color:inherit;text-decoration:none}

/* header */
.site-header{position:absolute;left:0;top:0;width:1200px;height:86px;background:var(--white);z-index:2}
.brand{position:absolute;left:48px;top:29px;display:flex;align-items:center;gap:10px;font-family:"Jost",sans-serif;font-weight:500;font-size:22px;color:var(--blue)}
.brand-mark{width:22px;height:22px;background:var(--blue)}
.main-nav{position:absolute;left:398px;top:44px;display:flex;font-family:"Jost",sans-serif;font-size:15px;color:var(--ink)}
.main-nav a{padding:0 14px;border-left:1px solid #777;line-height:14px}
.main-nav a:first-child{border-left:none;color:var(--blue);padding-left:0;text-decoration:underline;text-underline-offset:6px}
.btn-contact{position:absolute;left:963px;top:34px;width:175px;height:36px;background:var(--blue);color:#fff;font-family:"Jost",sans-serif;font-weight:500;font-size:15px;display:flex;align-items:center;justify-content:center;gap:20px;border-radius:2px}

/* photo placeholders */
.photo{border-radius:0 0 30px 0}
.photo-hero{background:
  radial-gradient(ellipse 260px 330px at 800px 300px,#c9b09a 0%,rgba(201,176,154,0) 70%),
  radial-gradient(ellipse 400px 300px at 300px 200px,#8e9aa4 0%,rgba(142,154,164,0) 75%),
  linear-gradient(135deg,#4f5a63 0%,#7d8890 40%,#5d6f78 65%,#2f363e 100%)}
.photo-about{background:
  radial-gradient(ellipse 180px 260px at 360px 230px,#3b4a63 0%,rgba(59,74,99,0) 80%),
  radial-gradient(ellipse 260px 200px at 90px 110px,#ecdcc4 0%,rgba(236,220,196,0) 80%),
  linear-gradient(135deg,#d8bfa0 0%,#a88a6c 45%,#4a4e5a 75%,#27303e 100%)}
.photo-why{background:
  radial-gradient(ellipse 160px 220px at 150px 190px,#2e4f86 0%,rgba(46,79,134,0) 80%),
  radial-gradient(ellipse 170px 200px at 440px 230px,#d9a98c 0%,rgba(217,169,140,0) 80%),
  radial-gradient(ellipse 140px 160px at 300px 120px,#6f6a6c 0%,rgba(111,106,108,0) 80%),
  linear-gradient(120deg,#e6e8ec 0%,#9aa5b6 50%,#c7a18c 100%)}
.photo-team{border-radius:48% 52% 50% 46%;background:
  radial-gradient(ellipse 120px 100px at 220px 170px,#dfe3e8 0%,rgba(223,227,232,0) 80%),
  radial-gradient(ellipse 160px 140px at 190px 260px,#7b5a4a 0%,rgba(123,90,74,0) 80%),
  linear-gradient(150deg,#2a3446 0%,#5b6575 45%,#2c3648 100%)}

/* hero */
.hero{position:absolute;left:0;top:86px;width:1200px;height:629px}
.hero-title{position:absolute;left:30px;top:185px;width:475px;text-align:center;font-family:"Jost",sans-serif;font-weight:600;font-size:48px;line-height:58px;color:#fff}
.hero-sub{position:absolute;left:30px;top:322px;width:475px;text-align:center;font-family:"Jost",sans-serif;font-size:22px;line-height:31px;color:#fff}
.btn-outline{position:absolute;left:204px;top:407px;width:130px;height:38px;border:1.5px solid #fff;background:var(--blue);color:#fff;font-size:13px;display:flex;align-items:center;justify-content:center;border-radius:2px}

/* common */
.eyebrow{font-family:"Jost",sans-serif;font-weight:500;font-size:20px;color:var(--ink)}
.heading{font-family:"Jost",sans-serif;font-weight:400;font-size:36px;color:var(--ink)}
.heading b{color:var(--blue);font-weight:600}
.body-text{font-size:13.5px;line-height:20px;color:var(--muted)}
.btn-solid{background:var(--blue);color:#fff;font-family:"Jost",sans-serif;font-weight:500;font-size:15px;display:flex;align-items:center;justify-content:center;border-radius:2px}
.link-more{font-family:"Jost",sans-serif;font-weight:500;font-size:15px;color:var(--blue)}

/* services */
.service{position:absolute;width:420px;text-align:center}
.service h3{font-family:"Jost",sans-serif;font-weight:500;font-size:18px;color:var(--ink);margin:18px 0 12px}
.service p{font-size:13.5px;line-height:20px}
.service .link-more{display:block;margin-top:26px}

/* why */
.why-list{position:absolute;left:66px;top:2036px;width:490px;list-style:none}
.why-list li{position:relative;padding-left:24px;font-size:13.5px;line-height:20px;margin-bottom:10px}
.why-list li::before{content:"";position:absolute;left:-2px;top:50%;width:9px;height:9px;border:3px solid var(--blue);border-radius:50%;transform:translateY(-50%)}

/* leaders */
.leader{position:absolute;width:320px;text-align:center}
.leader h3{font-family:"Jost",sans-serif;font-weight:500;font-size:22px;color:var(--ink);margin:36px 0 14px}
.leader p{font-size:13.5px;line-height:20px}
.leader .link-more{display:block;margin-top:26px}
.avatar{width:212px;height:212px;border-radius:50%;margin:0 auto;background:radial-gradient(circle at 50% 40%,var(--blue-soft) 0%,var(--blue) 55%,var(--blue-dark) 100%)}

/* footer */
.site-footer{position:absolute;left:0;top:3300px;width:1200px;height:478px;background:linear-gradient(180deg,#f5f7fa,var(--footer-bg))}
.footer-col h4{font-family:"Jost",sans-serif;font-weight:500;font-size:19px;color:var(--ink);text-decoration:underline;text-underline-offset:4px;margin-bottom:16px}
.footer-col li{list-style:none;font-size:13.5px;line-height:20px;margin-bottom:16px;padding-left:18px;position:relative}
.footer-col li::before{content:"‹";position:absolute;left:0;top:-2px;font-size:18px;color:var(--blue)}
.contact-row{display:flex;gap:12px;font-size:13.5px;line-height:20px;margin-bottom:14px}
.contact-row svg{flex:none;margin-top:2px}
.copyright{position:absolute;left:0;top:3688px;width:1200px;text-align:center;font-size:13.5px}
</style>
</head>
<body>

<header class="site-header">
  <div class="brand"><span class="brand-mark"></span>Vellora Consulting</div>
  <nav class="main-nav">
    <a href="#">Home</a><a href="#">About Us</a><a href="#">Our Services ▾</a><a href="#">Why Vellora?</a><a href="#">Vellora Leadership</a>
  </nav>
  <a class="btn-contact" href="#">Contact Us <span>⊕</span></a>
</header>

<section class="hero">
  <div class="abs photo-hero" role="img" aria-label="Smiling professional in an office with colleagues working behind him" style="left:0;top:0;width:1200px;height:629px"></div>
  <svg class="abs" style="left:0;top:0" width="1200" height="629" viewBox="0 0 1200 629">
    <polygon points="0,398 293,623 1200,414 1200,629 0,629" fill="var(--blue)"/>
    <polygon points="0,430 293,629 1200,430 1200,629 0,629" fill="var(--blue)"/>
    <polygon points="0,520 280,629 0,629" fill="#ffffff"/>
    <polygon points="310,629 1200,455 1200,629" fill="#ffffff"/>
  </svg>
  <h1 class="hero-title">Welcome To Vellora Consulting</h1>
  <p class="hero-sub">A Software Consulting Company Specializing In Serving Small To Medium Size Businesses</p>
  <a class="btn-outline" href="#">Explore More</a>
</section>

<!-- about -->
<section>
  <div class="abs photo photo-about" role="img" aria-label="Two businessmen reviewing a tablet in a meeting room" style="left:47px;top:783px;width:546px;height:390px"></div>
  <p class="abs eyebrow" style="left:647px;top:780px">About Us</p>
  <h2 class="abs heading" style="left:647px;top:816px">Who We <b>Are?</b></h2>
  <p class="abs body-text" style="left:647px;top:875px;width:506px;text-align:justify">Welcome to Vellora, a software consulting company specializing in serving small to medium size businesses. We understand the unique challenges and opportunities that these companies face, and we are dedicated to helping them succeed through innovative technology solutions.</p>
  <p class="abs body-text" style="left:647px;top:966px;width:506px;text-align:justify">Our team of experienced professionals has a diverse range of skills and expertise, making us well-equipped to handle any project, big or small. We specialize in custom software development, working closely with our clients to understand their specific needs and build solutions that meet their requirements.</p>
  <a class="abs btn-solid" href="#" style="left:647px;top:1093px;width:140px;height:38px">Know More »</a>
</section>

<!-- services -->
<section>
  <p class="abs eyebrow" style="left:0;width:1200px;text-align:center;top:1310px">Our Services</p>
  <h2 class="abs heading" style="left:0;width:1200px;text-align:center;top:1348px">How We <b>Serve You?</b></h2>
  <p class="abs body-text" style="left:47px;top:1406px;width:1106px">Vellora is a leading provider of economical custom software development and staff augmentation services. We specialize in helping companies around the world access top talent in the field of software development at an affordable price, without the hassle and expense of in-house hiring or managing remote employees.</p>
  <a class="abs link-more" href="#" style="left:70px;top:1480px">Read More »</a>

  <div class="service" style="left:167px;top:1540px">
    <svg width="64" height="62" viewBox="0 0 64 62" fill="none" stroke="var(--blue)" stroke-width="2">
      <path d="M22 44c-6-4-10-10-10-17a20 20 0 0 1 40 0c0 7-4 13-10 17v6H22z"/><path d="M24 54h16M26 58h12"/>
      <circle cx="40" cy="22" r="6"/><circle cx="40" cy="22" r="10" stroke-dasharray="4 3"/><path d="M4 20h6M54 20h6M32 2v5"/>
    </svg>
    <h3>Custom Solution Delivery</h3>
    <p>Vellora offers a range of services focused on helping businesses and organizations deliver software solutions to their customers or users..</p>
    <a class="link-more" href="#">Know More »</a>
  </div>
  <div class="service" style="left:612px;top:1540px">
    <svg width="64" height="62" viewBox="0 0 64 62" fill="none" stroke="var(--blue)" stroke-width="2">
      <circle cx="32" cy="31" r="9"/><circle cx="32" cy="31" r="14" stroke-dasharray="5 3"/>
      <circle cx="9" cy="8" r="5"/><circle cx="55" cy="8" r="5"/><circle cx="9" cy="54" r="5"/><circle cx="55" cy="54" r="5"/>
      <path d="M13 12l8 8M51 12l-8 8M13 50l8-8M51 50l-8-8"/>
    </svg>
    <h3>Staff Augmentation</h3>
    <p>Let Vellora help you supplement your existing software development teams with additional resources and expertise. We provided access to experienced</p>
    <a class="link-more" href="#">Know More »</a>
  </div>
</section>

<!-- why -->
<section>
  <p class="abs eyebrow" style="left:0;width:1200px;text-align:center;top:1925px">Why Vellora?</p>
  <h2 class="abs heading" style="left:0;width:1200px;text-align:center;top:1962px">Why You <b>Chose Us?</b></h2>
  <ul class="why-list">
    <li>At Vellora, we are proud to have a team of seasoned IT professionals who understand what it takes to deliver a quality solution.</li>
    <li>Our team members have a wealth of experience and expertise in a variety of different areas, including software development, system integration, data migration, and software maintenance and support.</li>
    <li>We understand that delivering a high-quality software solution requires more than just technical expertise.</li>
    <li>It also requires a deep understanding of the needs and challenges of our clients, and the ability to work closely with them to develop a solution that meets their specific requirements.</li>
    <li>Our team members are committed to delivering excellence in everything they do, and they are always looking for ways to improve processes and drive results.</li>
  </ul>
  <a class="abs btn-solid" href="#" style="left:66px;top:2382px;width:142px;height:36px">Know More »</a>
  <div class="abs photo photo-why" role="img" aria-label="Business partners shaking hands across a meeting table" style="left:608px;top:2039px;width:525px;height:375px"></div>
</section>

<!-- leadership -->
<section>
  <p class="abs eyebrow" style="left:0;width:1200px;text-align:center;top:2576px">Vellora Leadership</p>
  <h2 class="abs heading" style="left:0;width:1200px;text-align:center;top:2612px">Meet Our <b>Leader</b></h2>
  <div class="abs photo-team" role="img" aria-label="Overhead view of a team working around a round desk with laptops and documents" style="left:18px;top:2725px;width:392px;height:420px"></div>

  <div class="leader" style="left:439px;top:2708px">
    <div class="avatar" role="img" aria-label="Portrait placeholder for Dorian"></div>
    <h3>Dorian</h3>
    <p>As a leader, Dorian is dedicated to fostering a culture of collaboration, innovation, and excellence within his team. He believes that by empowering his team members and encouraging open communication, he can create an environment that is conducive to creativity and problem-solving.</p>
    <a class="link-more" href="#">Know More »</a>
  </div>
  <div class="abs" style="left:767px;top:2694px;width:1px;height:500px;background:#888"></div>
  <div class="leader" style="left:801px;top:2708px">
    <div class="avatar" role="img" aria-label="Portrait placeholder for Tomas"></div>
    <h3>Tomas</h3>
    <p>As a leader, Tomas is dedicated to fostering a culture of collaboration, innovation, and excellence within his team. He believes that by empowering his team members and encouraging open communication, he can create an environment that is conducive to creativity and problem-solving.</p>
    <a class="link-more" href="#">Know More »</a>
  </div>
</section>

<footer class="site-footer">
  <div class="abs" style="left:82px;top:118px;display:flex;align-items:center;gap:10px;font-family:'Jost',sans-serif;font-weight:500;font-size:22px;color:var(--blue)"><span style="width:24px;height:24px;background:var(--blue)"></span>Vellora Consulting</div>
  <p class="abs body-text" style="left:82px;top:190px;width:224px;text-align:justify">Welcome to Vellora, a software consulting company specializing in serving small to medium size businesses.</p>
  <a class="abs link-more" href="#" style="left:152px;top:300px;font-size:14px">Know More »</a>

  <div class="abs footer-col" style="left:402px;top:118px">
    <h4>Our Company</h4>
    <ul><li>About Us</li><li>Why Vellora?</li><li>Vellora Leadership</li><li>Testimonials</li></ul>
  </div>
  <div class="abs footer-col" style="left:680px;top:118px">
    <h4>Our Services</h4>
    <ul><li>Custom Solution Delivery</li><li>Staff Augmentation</li></ul>
  </div>
  <div class="abs footer-col" style="left:893px;top:118px;width:240px">
    <h4 style="margin-left:65px">Contact Us</h4>
    <div class="contact-row"><svg width="18" height="20" viewBox="0 0 18 20" fill="none" stroke="var(--blue)" stroke-width="1.5"><path d="M9 19s7-7 7-11A7 7 0 0 0 2 8c0 4 7 11 7 11z"/><circle cx="9" cy="8" r="2.5"/></svg><span>#88 Larkspur Avenue, Chicago</span></div>
    <div class="contact-row"><svg width="18" height="16" viewBox="0 0 18 16" fill="none" stroke="var(--blue)" stroke-width="1.5"><rect x="1" y="2" width="16" height="12"/><path d="M1 2l8 7 8-7"/></svg><span>support@brindlewave.example</span></div>
    <div class="contact-row"><svg width="18" height="18" viewBox="0 0 18 18" fill="none" stroke="var(--blue)" stroke-width="1.5"><path d="M4 1l3 4-2 2c1 3 3 5 6 6l2-2 4 3-2 3C8 17 1 10 1 3z"/></svg><span>+1 55501 234 876</span></div>
  </div>
</footer>
<p class="copyright">Copyright © 2022 brindlewave | Powered by brindlewave</p>

</body>
</html>
```